New Wedding Decor Web Design Project - GUARANTEED PAYMENT

We need to have a business website for a brand new wedding decor & events company, Lirovelle. We have just established our logo and would love to use this logo on the website.

Because this is a new business venture, we do not have too many pictures to post online. It'd be exciting what your creativity can bring us!

Our website is: www.Lirovelle.ca

Target Market(s)

Our clientele demographic is targeted to brides and bridesmaids in their 20-30 years old.

Industry/Entity Type

Wedding

Requirements
Must have
• - Professional, elegant and artistic look
- Modern feeling
- Very catchy flash intro page
- Ability to show Chatterbook posts
Nice to have
• - Easy to navigate, crisp and clean
- Live vocaline messaging or online messaging

I would like to have navigation pages like: Lirovelle Brand, Collections, Features, Contact Us, etc.

Each page I want it to be clean and easy to read. Something like the following website: http://www.pardunetho.com/

We offer:
BACKDROPS
HEAD, CAKE & RECEIVING TABLES DECOR
CHAIRCOVERS
TABLE CLOTHS & OVERLAYS
NAPKINS
CENTREPIECES
CEREMONY SET-UP
CANDELABRA
CRYSTAL GLOBES
LED LIGHTING
CUSTOM DESIGN AISLE RUNNERS
CAKE STANDS
MONEY BOX
CHARGERS
GOBO LIGHTING
Should not have
• - traditional, old style website
- very static (dull)
- too many images or busy layout
- no "standardized" website templates such as: www.brintaq.com/gallery/weddings

```html
<!DOCTYPE html>
<html lang="en">
<head>
<meta charset="utf-8">
<title>Lirovelle — Wedding Events</title>
<link rel="stylesheet" href="https://fonts.googleapis.com/css2?family=Questrial&family=Arimo&display=swap">
<style>
  :root {
    --pink: #ec5fb4;
    --pink-bar: #f27cc6;
    --text-grey: #555555;
    --logo-grey: #7b7b7b;
    --footer-grey: #5a5a5a;
    --icon-grey: #5c5c5c;
    --arrow-bg: rgba(190, 190, 190, 0.85);
    --white: #ffffff;
  }
  * { margin: 0; padding: 0; box-sizing: border-box; }
  html, body { width: 1200px; height: 873px; overflow: hidden; background: var(--white); }
  body { position: relative; font-family: "Questrial", sans-serif; }

  .top-bar { position: absolute; left: 0; top: 0; width: 1200px; height: 4px; background: var(--pink-bar); }

  .site-header { position: absolute; left: 0; top: 4px; width: 1200px; height: 144px; background: var(--white); }
  .brand { position: absolute; left: 118px; top: 16px; width: 200px; height: 122px; }
  .brand-mark { position: absolute; left: 12px; top: 0; width: 78px; height: 68px; border-radius: 50%; background: var(--pink); }
  .brand-name { position: absolute; left: 0; top: 64px; font-size: 42px; line-height: 42px; color: var(--logo-grey); letter-spacing: -0.5px; }
  .brand-tagline { position: absolute; right: 0; top: 104px; font-size: 14px; color: var(--logo-grey); letter-spacing: 0.3px; }

  .main-nav { position: absolute; top: 66px; left: 0; }
  .main-nav a { position: absolute; top: 0; white-space: nowrap; font-size: 14px; letter-spacing: 0.4px; color: var(--text-grey); text-decoration: none; }
  .main-nav a.is-active { color: var(--pink); }
  .main-nav a.is-active::after { content: ""; position: absolute; left: -8px; right: -8px; top: 27px; height: 3px; background: var(--pink); }

  .hero { position: absolute; left: 0; top: 148px; width: 1200px; height: 660px; overflow: hidden; }
  .hero-photo {
    position: absolute; inset: 0;
    background:
      radial-gradient(ellipse 420px 300px at 520px 340px, rgba(150, 90, 255, 0.55), transparent 70%),
      radial-gradient(ellipse 260px 420px at 880px 250px, rgba(245, 200, 240, 0.45), transparent 70%),
      linear-gradient(180deg, #6a3f7a 0%, #5a2fa0 45%, #7a4ed0 75%, #3c2260 100%);
  }
  .hero-caption {
    position: absolute; left: 118px; top: 254px; width: 660px;
    font-size: 25px; line-height: 37px; color: var(--white); text-transform: uppercase; letter-spacing: 0.2px;
  }
  .hero-arrow { position: absolute; top: 302px; width: 40px; height: 40px; }
  .hero-arrow.prev { left: 37px; }
  .hero-arrow.next { left: 1121px; }

  .site-footer { position: absolute; left: 0; top: 808px; width: 1200px; height: 65px; font-family: "Arimo", sans-serif; color: var(--footer-grey); }
  .footer-links { position: absolute; left: 121px; top: 11px; font-size: 12px; }
  .footer-links a { color: var(--footer-grey); text-decoration: none; }
  .copyright { position: absolute; left: 121px; top: 36px; font-size: 12px; }
  .social { position: absolute; left: 924px; top: 18px; display: flex; gap: 5px; }
  .social span { width: 26px; height: 26px; border-radius: 50%; background: var(--icon-grey); display: block; }
</style>
</head>
<body>
  <div class="top-bar"></div>

  <header class="site-header">
    <div class="brand">
      <span class="brand-mark"></span>
      <span class="brand-name">Lirovelle</span>
      <span class="brand-tagline">wedding events</span>
    </div>
    <nav class="main-nav">
      <a class="is-active" href="#" style="left:441px">HOME</a>
      <a href="#" style="left:537px">LIROVELLE BRAND</a>
      <a href="#" style="left:719px">COLLECTIONS</a>
      <a href="#" style="left:865px">FEATURES</a>
      <a href="#" style="left:982px">CONTACT US</a>
    </nav>
  </header>

  <section class="hero">
    <div class="hero-photo" role="img" aria-label="Wedding ceremony aisle with crystal trees, draped fabric and chair covers under purple LED lighting"></div>
    <p class="hero-caption">We provide all these services backdrops, head, cake &amp; receiving tables décor, chaircovers, table cloths &amp; overlays, napkins, crystal globes, LED lighting, cake stands</p>
    <svg class="hero-arrow prev" viewBox="0 0 40 40" aria-label="Previous slide">
      <circle cx="20" cy="20" r="20" fill="var(--arrow-bg)"/>
      <path d="M23 11 L14 20 L23 29" fill="none" stroke="#333" stroke-width="3.5" stroke-linecap="round" stroke-linejoin="round"/>
    </svg>
    <svg class="hero-arrow next" viewBox="0 0 40 40" aria-label="Next slide">
      <circle cx="20" cy="20" r="20" fill="var(--arrow-bg)"/>
      <path d="M17 11 L26 20 L17 29" fill="none" stroke="#333" stroke-width="3.5" stroke-linecap="round" stroke-linejoin="round"/>
    </svg>
  </section>

  <footer class="site-footer">
    <div class="footer-links"><a href="#">Sitemap</a> | <a href="#">Privacy</a> | <a href="#">Terms of Use</a></div>
    <div class="copyright">© 2013 &nbsp;| &nbsp;Lirovelle. All Rights Reserved.</div>
    <div class="social" aria-label="Social links">
      <span></span><span></span><span></span><span></span><span></span>
    </div>
  </footer>
</body>
</html>
```